Meadowlark Counseling Partners, LLC Needs Modern Business Card Design.

We provide behavioral health services from western Kansas to eastern Kansas. There is an abundance of competition for the services we provide with our main competitor being larger and having significantly more financial resources; however, the quality of services we provide is greater and we have started to catch the attention of the State of Kansas. We had a great logo designed by ArtFolio - this will be used to build upon our brand. The logo (attached) should be used in the card development. We want something unique, modern, but also a card design that clearly states our name, contact info, provides the name and unqiue location of each clinician, etc. Rounded edges, or a unique size, just something that makes our business card stand out from others. I have also uploaded each clinician's name and their unique location and phone number.

Our idea is to have one side be black with our logo. Then, on the other side have business cards for each individual. Plus, we want one card that is "generic" with no specific clinician's name listed so that we can give clients an appointment card when they leave. Some clinicians have two locations - we're open to design and background color, but we have started going with branding colors of black, the yellow in the logo files attached, and sometimes a gray. Our new office has been decorated using this theme.

Target Market(s)

individuals and families in need of behavioral health services; potential professional referral sources; existing referral sources

Industry/Entity Type

Business

Contact Information for Business Card

I attached a Word doc that provides clinician names, credentials and location information specific to each individual.

Font styles to use
Serif

Colors
000000
fbed22
dbdbdb
9d9d9d
c3c3c3

Requirements
Must have
• 1) use of the company logo that has been attached; 2) a template that provides us space to individualize business cards for all of our clinicians; 3) should stick to the colors we are branding with: black, yellow from the logo file, maybe a gray shade and we're open to a suggestion on a shade of white.
Nice to have
• Group discussion culminated in the thought that one side would be black with just our logo - no clinician names, etc. A unique design - rounded edges, unique size, some catchy lay-out would be nice.
Should not have
• Must not be too busy. Should look "clean." The project should stick to branding colors: black, yellow (from the logo file), maybe a gray and shade of white.

```html
<!DOCTYPE html>
<html lang="en">
<head>
<meta charset="utf-8">
<title>Meadowlark Counseling Partners – Business Card</title>
<link rel="stylesheet" href="https://fonts.googleapis.com/css2?family=Crimson+Pro:wght@600&family=Source+Sans+3:wght@400;700&display=swap">
<style>
  :root {
    --backdrop: #d1d2d4;
    --card-white: #ffffff;
    --card-charcoal: #3a3a3c;
    --brand-gold: #f9c100;
    --rule-gray: #c3c3c3;
    --text-gray: #555557;
    --serif: "Crimson Pro", Georgia, serif;
    --sans: "Source Sans 3", Arial, sans-serif;
  }
  * { margin: 0; padding: 0; box-sizing: border-box; }
  html, body {
    width: 1200px; height: 1200px; overflow: hidden;
    background: var(--backdrop);
  }
  .stage { position: relative; width: 1200px; height: 1200px; }

  .card {
    position: absolute;
    width: 707px; height: 423px;
    border-radius: 32px;
    overflow: hidden;
  }
  .card--front { left: 232px; top: 100px; background: var(--card-white); }
  .card--back  { left: 237px; top: 645px; background: var(--card-charcoal); }

  /* Front */
  .brand-block {
    position: absolute; left: 263px; top: 124px; width: 375px;
    font-family: var(--serif); font-weight: 600; color: var(--brand-gold);
  }
  .brand-block__name { font-size: 42px; line-height: 1; letter-spacing: 2.5px; }
  .brand-block__sub { font-size: 19px; line-height: 1; letter-spacing: 1.6px; margin-top: 8px; }
  .brand-block__rule {
    height: 1px; background: var(--rule-gray); margin-top: 15px;
  }

  .contact {
    position: absolute; right: 78px; top: 241px;
    text-align: right; font-family: var(--sans); color: var(--text-gray);
    font-size: 21px; line-height: 29.6px;
  }
  .contact__name { font-weight: 700; letter-spacing: 0.2px; }

  /* Back */
  .brand-mark {
    position: absolute; left: 50%; top: 108px; transform: translateX(-50%);
    width: 96px; height: 96px; border-radius: 50%;
    background: var(--brand-gold);
  }
  .brand-lockup {
    position: absolute; left: 0; right: 0; top: 230px;
    text-align: center; font-family: var(--serif); font-weight: 600;
    color: var(--brand-gold);
  }
  .brand-lockup__name { font-size: 48px; line-height: 1; letter-spacing: 3px; }
  .brand-lockup__sub { font-size: 25px; line-height: 1; letter-spacing: 2px; margin-top: 8px; }
</style>
</head>
<body>
<main class="stage">
  <section class="card card--front" aria-label="Business card front">
    <div class="brand-block">
      <div class="brand-block__name">MEADOWLARK</div>
      <div class="brand-block__sub">COUNSELING PARTNERS, LLC</div>
      <div class="brand-block__rule"></div>
    </div>
    <address class="contact" style="font-style: normal;">
      <div class="contact__name">DANIEL R. WHITCOMB, LP</div>
      <div>President</div>
      <div>418 N. Elm Ave.</div>
      <div>Wichita Kansas 67203</div>
      <div>316.555.0182</div>
    </address>
  </section>

  <section class="card card--back" aria-label="Business card back">
    <div class="brand-mark"></div>
    <div class="brand-lockup">
      <div class="brand-lockup__name">MEADOWLARK</div>
      <div class="brand-lockup__sub">COUNSELING PARTNERS, LLC</div>
    </div>
  </section>
</main>
</body>
</html>
```